Verdant Pathworks Business Card

want the back of card to be blue- with the logo in the center
front of card- info plus logo (info being mailing address, email address, and website address )
4 different names with titles to have on cards
1) Dominic Ashvale - Owner
2) Bethany Korvuth- Customer Relationship Specialist
3) Luca Brennwick- Vice President of Sales
4) Neil Umbright- Chief Technology Officer

Target Market(s)

tech company in the government/probation office industry

Industry/Entity Type

Government Office

Contact Information for Business Card

1) Dominic Ashvale - Owner

Colors
0355a3
ffffff

Requirements
Must have
• back side should be blue, with the logo placed in the center
• front side needs to include both the logo, as well as company info (info should include website address, email address, and mailing address)

```html
<!DOCTYPE html>
<html lang="en">
<head>
<meta charset="utf-8">
<title>Verdant Pathworks Business Card</title>
<link href="https://fonts.googleapis.com/css2?family=Roboto:wght@400;700&display=swap" rel="stylesheet">
<style>
  :root {
    --backdrop: #8c8c8c;
    --card-white: #ffffff;
    --navy: #1a2d5a;
    --card-blue: #182c54;
    --ink: #222222;
    --rule: #4a4f5c;
  }
  * { margin: 0; padding: 0; box-sizing: border-box; }
  html, body {
    width: 1200px; height: 1200px; overflow: hidden;
    background: var(--backdrop);
    font-family: "Roboto", Arial, sans-serif;
  }
  .card {
    position: absolute; top: 310px; height: 594px;
    box-shadow: 2px 3px 6px rgba(0,0,0,0.45);
  }
  .card-front { left: 234px; width: 364px; background: var(--card-white); }
  .card-back { left: 627px; width: 369px; background: var(--card-blue); }
  .brand {
    position: absolute; left: 0; right: 0; text-align: center;
    font-weight: 400; font-size: 30px; line-height: 34px;
    letter-spacing: 3px; text-transform: uppercase;
  }
  .card-front .brand { top: 112px; color: var(--navy); }
  .card-back .brand { top: 310px; color: var(--card-white); }
  .brand-mark {
    position: absolute; left: 50%; top: 230px; width: 56px; height: 56px;
    margin-left: -28px; border: 3px solid var(--card-white); border-radius: 50%;
  }
  .team { position: absolute; top: 254px; left: 0; right: 0; text-align: center; }
  .member { margin-bottom: 6px; }
  .member-name {
    font-weight: 700; font-size: 21px; line-height: 24px; color: var(--navy);
  }
  .member-title { font-size: 16px; line-height: 19px; color: var(--ink); }
  .rule {
    position: absolute; left: 44px; width: 270px; height: 1px; background: var(--rule);
  }
  .rule-top { top: 458px; }
  .rule-bottom { top: 511px; }
  .contact, .address {
    position: absolute; left: 0; right: 0; text-align: center;
    font-size: 16.5px; line-height: 21px; color: var(--ink);
  }
  .contact { top: 462px; }
  .address { top: 516px; }
</style>
</head>
<body>
  <section class="card card-front">
    <div class="brand">Verdant<br>Pathworks</div>
    <div class="team">
      <div class="member"><div class="member-name">DOMINIC ASHVALE</div><div class="member-title">Owner</div></div>
      <div class="member"><div class="member-name">BETHANY KORVUTH</div><div class="member-title">Customer Relationship Specialist</div></div>
      <div class="member"><div class="member-name">LUCA BRENNWICK</div><div class="member-title">Vice President of Sales</div></div>
      <div class="member"><div class="member-name">NEIL UMBRIGHT</div><div class="member-title">Chief Technology Officer</div></div>
    </div>
    <div class="rule rule-top"></div>
    <div class="contact">support@VerdantPathworks.com<br>www.VerdantPathworks.com</div>
    <div class="rule rule-bottom"></div>
    <div class="address">421, Address line here,<br>45452,Country Name</div>
  </section>
  <section class="card card-back">
    <div class="brand-mark"></div>
    <div class="brand">Verdant<br>Pathworks</div>
  </section>
</body>
</html>
```